Starter & Alternator business needs a website

update: very good designs submitted so far. also need this to display well on mobile devices. not sure if wordpress or html/css is better for my needs.

Our existing website is vellumtorq.com and is need of total revamp. Need full design of a website for my business.

We sell and rebuild starters and alternators. Customers bring in the units and we rebuild them. Or we sell them brand new or rebuilt units we have in stock. We do not install units into vehicles like a mechanic would. We strictly rebuild starters and alternators in our shop, sell brand new units over the counter, and we do deliver occasionally as well. We do offer a line of Orvan batteries as well but that is only a small feature of the business.

I would like this website designed and coded. I can upload the files to my web host after completion. I can also add in and modify content like our background info, etc.

I have included an illustrator file that shows some of our signage and logo, etc. I have also included a radio commercial sample so you can get a little better feel for the business. A similar ad does run on the radio currently, slightly different and without the added sound effects.

Update: I do like using photos of real items(starters or alternators etc) for an icon, like a real alternator stock image for the alternator section icon, etc. Maybe incorporate our logo in that design as well. That looks nice as well and may aid in navigation.

For any other design elements, do what you think looks good. Our colors are red/white/blue as seen in the illustrator file. our building is painted with halbeck moray colors, ember gala red and deep tide for blue.

Here are some examples of rebuilders websites in other markets for reference:

https://quillmarauto.com/starter-alternator-rebuilding/

https://www.dunwickmotorworks.com/auto-repairs/alternator-starter-rebuilds.aspx

https://www.fjordvoltage.com/

https://www.pemberlowgx.com/

The website can have areas for: services and products offered, high output alternators, Orvan Batteries, troubleshooting tips, current specials, contact info and directions/map, etc. Whatever else you feel applies.

At some point I do want to be able to sell items directly online or at least have a secure section for customers to submit invoice payments, but that's not necessarily in scope for this project just something to keep in mind.

Target Market(s)

Mechanics and Managers in fleet shops, construction and marine industries, shipping trades. Also automobile owners who work on their own vehicles. We sell and rebuild starters and alternators for automobiles, heavy duty equipment, forklifts, traxlifts, man movers, ferrettes, loaders, large tractors and trucks, just about any engine, golf carts, generators, etc.

Industry/Entity Type

Automotive Part

Coding

Coded - Design and coding required

Number of Pages Required

5+ page

Font styles to use
Serif
Sans Serif

Colors
0255a3
ec1f27
ffffff

Requirements
Must have
• Should also display nicely on mobile phones. Highlight our specialty, "Starters & Alternators"

```html
<!DOCTYPE html>
<html lang="en">
<head>
<meta charset="utf-8">
<title>Harbor Crest Rebuilders — Starters &amp; Alternators</title>
<link rel="stylesheet" href="https://fonts.googleapis.com/css2?family=Bebas+Neue&family=Domine:wght@400;700&family=Nunito+Sans:wght@400;600&display=swap">
<style>
:root{
  --red:#c8232b;
  --red-bright:#e8262e;
  --navy:#1b3262;
  --navy-deep:#172b55;
  --white:#ffffff;
  --ink:#555b66;
  --silver:#c3c6ca;
  --steel:#8d9197;
  --copper:#a4552c;
}
*{box-sizing:border-box;margin:0;padding:0}
html,body{width:1200px;height:3849px;overflow:hidden}
body{position:relative;font-family:"Nunito Sans",Arial,sans-serif;color:var(--ink);background:var(--white)}
.abs{position:absolute}
.center{text-align:center}

/* top bar */
.topbar{left:0;top:0;width:1200px;height:42px;background:linear-gradient(var(--red-bright),var(--red))}
.topbar .call{right:78px;top:0;height:42px;display:flex;align-items:center;gap:12px;color:var(--white);font-family:"Domine",Georgia,serif;font-size:17px}
.topbar .call .label{font-size:15px}
.phone-dot{width:30px;height:30px;border-radius:50%;background:var(--navy);display:flex;align-items:center;justify-content:center}

/* header */
.header{left:0;top:42px;width:1200px;height:98px;background:var(--white)}
.brand{left:78px;top:30px;display:flex;align-items:center;gap:12px;font-family:"Domine",Georgia,serif;font-weight:700;font-size:17px;color:var(--navy)}
.brand .dot{width:38px;height:38px;border-radius:50%;background:var(--red)}
.nav{right:72px;top:40px;display:flex;gap:30px;font-size:15px;color:#333;letter-spacing:.3px}
.nav .active{color:var(--red)}

/* hero */
.hero{left:0;top:140px;width:1200px;height:537px;background:linear-gradient(100deg,#c9cbce 0%,#b9bcc0 45%,#a9acb0 100%)}
.hero-photo{left:520px;top:0;width:680px;height:537px;background:
  radial-gradient(circle at 42% 50%,#e9e2cf 0 4%,#b9b2a0 6%,transparent 12%),
  radial-gradient(ellipse 38% 46% at 42% 52%,#dfe1e3 0%,#a7abb0 40%,#6f7379 62%,transparent 70%),
  radial-gradient(ellipse 30% 50% at 95% 35%,#c0c3c7,transparent 70%),
  linear-gradient(100deg,#b9bcc0,#a2a6ab 60%,#b7babe)}
.hero h1{left:78px;top:140px;font-family:"Bebas Neue",Impact,sans-serif;font-weight:400;font-size:76px;line-height:68px;color:var(--white);letter-spacing:1px}
.hero .lede{left:79px;top:290px;width:420px;font-size:19px;line-height:27px;color:#3d4148}
.btn{display:inline-flex;align-items:center;justify-content:center;background:var(--red);color:var(--white);font-family:"Domine",Georgia,serif;font-size:18px;border-radius:4px}
.hero .btn{left:77px;top:359px;width:177px;height:57px}
.arrow{width:52px;height:52px;border:2px solid rgba(255,255,255,.85);border-radius:50%;top:232px;display:flex;align-items:center;justify-content:center}

/* welcome */
.welcome{left:0;top:677px;width:1200px;height:415px}
.eyebrow{color:var(--red);font-family:"Domine",Georgia,serif;font-size:21px;letter-spacing:.5px}
.h2{color:var(--navy);font-family:"Domine",Georgia,serif;font-size:44px;font-weight:700;letter-spacing:.5px}
.welcome .eyebrow{left:0;width:1200px;top:65px}
.welcome .h2{left:0;width:1200px;top:98px}
.welcome p{left:250px;width:700px;top:158px;font-size:13.4px;line-height:27px}
.down{left:574px;top:291px;width:52px;height:52px;border-radius:50%;background:var(--red);display:flex;align-items:center;justify-content:center}

/* services */
.services{left:0;top:1092px;width:1200px;height:328px;background:var(--navy)}
.notch{left:567px;top:0;width:0;height:0;border-left:33px solid transparent;border-right:33px solid transparent;border-top:33px solid var(--white)}
.services h2{left:0;width:1200px;top:72px;color:var(--white);font-family:"Domine",Georgia,serif;font-weight:400;font-size:44px;letter-spacing:.5px}
.tab{top:154px;width:140px;height:145px;display:flex;flex-direction:column;align-items:center;justify-content:center;gap:18px;color:var(--white);font-family:"Domine",Georgia,serif;font-size:16px}
.tab.on{background:var(--red)}

/* photo band */
.photo-band{left:0;top:1420px;width:1200px;height:521px;background:
  radial-gradient(ellipse 14% 30% at 2% 75%,rgba(164,85,44,.75),transparent 70%),
  radial-gradient(ellipse 6% 9% at 75% 48%,rgba(214,182,58,.55),transparent 70%),
  radial-gradient(ellipse 45% 60% at 35% 40%,#a4a8ad 0%,#6d7278 55%,transparent 80%),
  linear-gradient(115deg,#3f444a 0%,#7b8086 35%,#5a5f65 55%,#2c3035 78%,#1f2226 100%)}

/* product cards */
.card{top:1944px;width:396px;height:291px}
.card .img{left:0;top:0;width:396px;height:233px;background:linear-gradient(#d3d5d8,#eef0f2 68%,#dfe1e3)}
.card .img i{position:absolute;border-radius:30px}
.card.sa .img i{left:62px;top:60px;width:260px;height:110px;background:radial-gradient(ellipse,#70757b,#b3b6ba 55%,transparent 72%)}
.card.bt .img i{left:108px;top:38px;width:190px;height:150px;background:radial-gradient(ellipse at 40% 45%,#3a3a3d,#1c1c1e 50%,rgba(190,30,40,.55) 62%,transparent 74%)}
.card.cb .img i{left:80px;top:40px;width:250px;height:140px;background:radial-gradient(ellipse,rgba(180,25,35,.85),rgba(200,130,90,.45) 50%,transparent 72%)}
.card .label{left:0;top:233px;width:396px;height:58px;background:linear-gradient(var(--red-bright),var(--red));color:var(--white);font-family:"Domine",Georgia,serif;font-size:19px;display:flex;align-items:center;justify-content:center;letter-spacing:.3px}

/* specials */
.specials .eyebrow{left:0;width:1200px;top:2293px;font-size:19px}
.specials .h2{left:0;width:1200px;top:2322px}
.specials p{left:250px;width:700px;top:2392px;font-size:13.4px;line-height:27px}
.specials-photo{left:0;top:2487px;width:1200px;height:404px;background:
  radial-gradient(ellipse 28% 50% at 60% 70%,#cfd2d5 0%,#8e9298 45%,transparent 75%),
  radial-gradient(ellipse 24% 34% at 28% 78%,#b8bbbf 0%,#6c7076 50%,transparent 78%),
  linear-gradient(100deg,#ffffff 0%,#ffffff 10%,#dadcde 30%,#b2b6ba 55%,#9b9fa4 80%,#4a4e53 100%)}
.cta-band{left:0;top:2891px;width:1200px;height:119px;background:var(--navy)}
.cta-band .btn{top:34px;height:53px;font-size:19px}

/* source */
.source h3{left:0;width:1200px;top:3075px;color:var(--navy);font-family:"Domine",Georgia,serif;font-weight:400;font-size:30px;line-height:42px;letter-spacing:.5px}
.source p{left:0;width:1200px;top:3178px;font-size:15px;color:#444}
.callrow{left:0;width:1200px;top:3233px;display:flex;align-items:center;justify-content:center;gap:18px;font-family:"Domine",Georgia,serif;color:var(--red)}
.callrow .t{font-size:29px}
.callrow .n{font-size:32px}
.callrow .ring{width:72px;height:72px;border-radius:50%;background:var(--red);display:flex;align-items:center;justify-content:center}

/* info bar */
.infobar{left:0;top:3369px;width:1200px;height:115px;background:linear-gradient(var(--red-bright),var(--red))}
.info{top:34px;display:flex;gap:14px;color:var(--white)}
.info h4{font-family:"Domine",Georgia,serif;font-weight:400;font-size:22px;line-height:26px}
.info span{font-size:13px}

/* footer */
.footer{left:0;top:3484px;width:1200px;height:365px;background:var(--navy-deep)}
.foot-brand{left:118px;top:80px;width:230px;display:flex;flex-direction:column;align-items:center;gap:12px;font-family:"Domine",Georgia,serif;font-weight:700;font-size:19px;color:var(--white);text-align:center;line-height:26px}
.foot-brand .dot{width:44px;height:44px;border-radius:50%;background:var(--red)}
.social{top:207px;width:46px;height:46px;border-radius:50%;background:var(--red);display:flex;align-items:center;justify-content:center}
.foot-h{font-family:"Domine",Georgia,serif;color:var(--white);font-size:21px;letter-spacing:.5px}
.prod-list{left:433px;top:86px;list-style:none;font-size:13px;color:#d9deea}
.prod-list li{height:31px;display:flex;align-items:center;gap:10px}
.prod-list li::before{content:"";width:5px;height:5px;border-radius:50%;background:var(--red-bright)}
.map{left:789px;top:79px;width:333px;height:177px;background:linear-gradient(135deg,#eef0f2,#e3e7ec 60%,#dde3ea);border:1px solid #c7ccd3}
.rule{left:0;top:297px;width:1200px;height:1px;background:rgba(255,255,255,.12)}
.copy{left:0;width:1200px;top:324px;font-size:13px;color:#c9cfdc}
</style>
</head>
<body>

<div class="abs topbar">
  <div class="abs call"><span class="label">CALL US NOW</span>
    <span class="phone-dot"><svg width="16" height="16" viewBox="0 0 24 24"><path d="M6.6 10.8a15 15 0 0 0 6.6 6.6l2.2-2.2c.3-.3.7-.4 1-.2 1.1.4 2.3.6 3.6.6.6 0 1 .4 1 1V20c0 .6-.4 1-1 1A17 17 0 0 1 3 4c0-.6.4-1 1-1h3.5c.6 0 1 .4 1 1 0 1.3.2 2.5.6 3.6.1.3 0 .7-.2 1z" fill="#fff"/></svg></span>
    <span>808-555-0142</span></div>
</div>

<header class="abs header">
  <div class="abs brand"><span class="dot"></span>Harbor Crest Rebuilders</div>
  <nav class="abs nav">
    <span class="active">&#9889; HOME</span><span>ABOUT</span><span>PRODUCTS</span><span>SERVICES</span><span>BLOG</span><span>CONTACT</span>
    <svg width="15" height="15" viewBox="0 0 20 20" style="margin-top:2px"><circle cx="8" cy="8" r="6" fill="none" stroke="#333" stroke-width="2.4"/><path d="M12.5 12.5l5 5" stroke="#333" stroke-width="2.6"/></svg>
  </nav>
</header>

<section class="abs hero">
  <div class="abs hero-photo" role="img" aria-label="Photo of a chrome alternator with copper windings"></div>
  <h1 class="abs">STARTERS &amp;<br>ALTERNATORS</h1>
  <p class="abs lede">Your source for New and High-Quality Rebuilt Starters &amp; Alternators.</p>
  <a class="abs btn">CONTACT US</a>
  <div class="abs arrow" style="left:10px"><svg width="14" height="22" viewBox="0 0 14 22"><path d="M12 1L2 11l10 10" fill="none" stroke="#fff" stroke-width="2"/></svg></div>
  <div class="abs arrow" style="left:1137px"><svg width="14" height="22" viewBox="0 0 14 22"><path d="M2 1l10 10L2 21" fill="none" stroke="#fff" stroke-width="2"/></svg></div>
</section>

<section class="abs welcome center">
  <div class="abs eyebrow">WELCOME TO</div>
  <h2 class="abs h2">HARBOR CREST REBUILDERS</h2>
  <p class="abs">Lorem Ipsum is simply dummy text of the printing and typesetting industry. Lorem Ipsum has been the industry's standard dummy text ever since the 1500s, when an unknown printer took a galley of type and scrambled it to make a type specimen book. It has survived not only five centuries, but also the leap into<br>Lorem Ipsum is simply dummy text of the.</p>
  <div class="abs down"><svg width="22" height="14" viewBox="0 0 22 14"><path d="M2 2l9 9 9-9" fill="none" stroke="#fff" stroke-width="2"/></svg></div>
</section>

<section class="abs services center">
  <div class="abs notch"></div>
  <h2 class="abs">OUR SERVICES</h2>
  <div class="abs tab" style="left:359px">
    <svg width="64" height="64" viewBox="0 0 64 64" fill="none" stroke="#fff" stroke-width="2"><circle cx="32" cy="32" r="30"/><circle cx="32" cy="32" r="22"/><circle cx="32" cy="32" r="6"/><path d="M32 10v16M32 38v16M10 32h16M38 32h16"/></svg>
    AUTOMOTIVE</div>
  <div class="abs tab on" style="left:529px">
    <svg width="56" height="64" viewBox="0 0 56 64" fill="none" stroke="#fff" stroke-width="2"><circle cx="28" cy="6" r="4"/><path d="M28 10v8M20 18h16l4 26H16zM14 44h28l6 10H8zM4 60h48"/><path d="M18 30h20"/></svg>
    MARINE</div>
  <div class="abs tab" style="left:704px">
    <svg width="64" height="64" viewBox="0 0 64 64" fill="none" stroke="#fff" stroke-width="2"><path d="M6 14h18l6 16v14H6zM30 30l14-18 10 6-6 10"/><path d="M48 28l8 12h-12z"/><circle cx="14" cy="50" r="7"/><path d="M6 56h28"/></svg>
    HEAVYA DUTY</div>
</section>

<div class="abs photo-band" role="img" aria-label="Close-up photo of an alternator housing, copper windings and a wired connector"></div>

<article class="abs card sa" style="left:0">
  <div class="abs img" role="img" aria-label="Photo of a starter and an alternator"><i></i></div>
  <div class="abs label">STARTERS &amp; ALTERNATORS</div>
</article>
<article class="abs card bt" style="left:402px">
  <div class="abs img" role="img" aria-label="Photo of a battery and inverter"><i></i></div>
  <div class="abs label">BATTERIES</div>
</article>
<article class="abs card cb" style="left:804px">
  <div class="abs img" role="img" aria-label="Photo of red and black battery jumper cables"><i></i></div>
  <div class="abs label">BATTERY CABLES</div>
</article>

<section class="specials center">
  <div class="abs eyebrow">HCROahu</div>
  <h2 class="abs h2">CURRENT SPECIALS</h2>
  <p class="abs">Lorem Ipsum is simply dummy text of the printing and typesetting industry. Lorem Ipsum has been the<br>industry's standard dummy text ever since the.</p>
  <div class="abs specials-photo" role="img" aria-label="Photo of a starter motor beside a large alternator"></div>
</section>

<div class="abs cta-band">
  <a class="abs btn" style="left:427px;width:166px">VIEW MORE</a>
  <a class="abs btn" style="left:601px;width:171px">CONTACT US</a>
</div>

<section class="source center">
  <h3 class="abs">YOUR SOURCE FOR NEW AND HIGH - QUALITY<br>REBUILT STARTERS &amp; ALTERNATORS.</h3>
  <p class="abs">Serving the Marine, Heavy Duty, Specialty, and Automotive industries.</p>
  <div class="abs callrow"><span class="t">CALL US NOW</span>
    <span class="ring"><svg width="34" height="34" viewBox="0 0 24 24"><path d="M6.6 10.8a15 15 0 0 0 6.6 6.6l2.2-2.2c.3-.3.7-.4 1-.2 1.1.4 2.3.6 3.6.6.6 0 1 .4 1 1V20c0 .6-.4 1-1 1A17 17 0 0 1 3 4c0-.6.4-1 1-1h3.5c.6 0 1 .4 1 1 0 1.3.2 2.5.6 3.6.1.3 0 .7-.2 1z" fill="#fff"/></svg></span>
    <span class="n">808-555-0142</span></div>
</section>

<section class="abs infobar">
  <div class="abs info" style="left:94px">
    <svg width="28" height="34" viewBox="0 0 28 34" fill="none" stroke="#fff" stroke-width="1.6"><path d="M14 32S3 20 3 12a11 11 0 0 1 22 0c0 8-11 20-11 20z"/><circle cx="14" cy="12" r="4"/></svg>
    <div><h4>ADDRESS</h4><span>417 Maleko St, Honolulu, HI 96819.</span></div></div>
  <div class="abs info" style="left:451px">
    <svg width="28" height="30" viewBox="0 0 24 24" fill="none" stroke="#fff" stroke-width="1.3"><path d="M6.6 10.8a15 15 0 0 0 6.6 6.6l2.2-2.2c.3-.3.7-.4 1-.2 1.1.4 2.3.6 3.6.6.6 0 1 .4 1 1V20c0 .6-.4 1-1 1A17 17 0 0 1 3 4c0-.6.4-1 1-1h3.5c.6 0 1 .4 1 1 0 1.3.2 2.5.6 3.6.1.3 0 .7-.2 1z"/></svg>
    <div><h4>CALL US</h4><span>808-555-0142</span></div></div>
  <div class="abs info" style="left:804px">
    <svg width="28" height="28" viewBox="0 0 28 28" fill="none" stroke="#fff" stroke-width="1.6"><circle cx="14" cy="14" r="12"/><path d="M14 6v8l5 4"/></svg>
    <div><h4>OPENING HOURS</h4><span>Mon-Fri 8-6pm, Sat 9-2pm.</span></div></div>
</section>

<footer class="abs footer">
  <div class="abs foot-brand"><span class="dot"></span>Harbor Crest<br>Rebuilders</div>
  <a class="abs social" style="left:180px" aria-label="Share">
    <svg width="20" height="20" viewBox="0 0 20 20" fill="#fff"><circle cx="15" cy="4" r="2.6"/><circle cx="5" cy="10" r="2.6"/><circle cx="15" cy="16" r="2.6"/><path d="M5 10l10-6M5 10l10 6" stroke="#fff" stroke-width="1.6"/></svg></a>
  <a class="abs social" style="left:234px" aria-label="Email">
    <svg width="20" height="16" viewBox="0 0 20 16" fill="none" stroke="#fff" stroke-width="1.8"><rect x="1" y="1" width="18" height="14" rx="1.5"/><path d="M1.5 2l8.5 7 8.5-7"/></svg></a>
  <div class="abs foot-h" style="left:433px;top:46px">OUR PRODUCTS</div>
  <ul class="abs prod-list">
    <li>Starters &amp; Alternators</li><li>Batteries</li><li>Battery Cables</li><li>High Output Alternators</li><li>Orvan Batteries</li><li>Troubleshooting Tips</li>
  </ul>
  <div class="abs foot-h" style="left:792px;top:46px">LOCATION MAP</div>
  <div class="abs map" role="img" aria-label="Street map showing the shop location"></div>
  <div class="abs rule"></div>
  <div class="abs copy center">&copy;HCROahu - 2019 All Rights Reserved.</div>
</footer>

</body>
</html>
```